Plumbing Business needs a more appealing business card design and logo

card must include phone number and logo, open to new logo ideas, full creative freedom

Industry/Entity Type

Plumbing

Contact Information for Business Card

Darrell Whitcombe
0417305829

Logo Text

call outs from $80

Font styles to use
• unsure

Colors
ec1f27
0255a3
f78f20

```html
<!DOCTYPE html>
<html lang="en">
<head>
<meta charset="utf-8">
<title>Corella Plumbing – Business Card</title>
<link rel="stylesheet" href="https://fonts.googleapis.com/css2?family=Montserrat:wght@600&family=Open+Sans:wght@700&display=swap">
<style>
  :root {
    --backdrop: #3b3b3b;
    --card-black: #1b1b1b;
    --card-white: #ffffff;
    --brand-orange: #f78f20;
    --brand-blue: #0255a3;
    --text-light: #ffffff;
  }
  * { margin: 0; padding: 0; box-sizing: border-box; }
  html, body {
    width: 1200px;
    height: 1200px;
    overflow: hidden;
    background: var(--backdrop);
  }
  .canvas {
    position: relative;
    width: 1200px;
    height: 1200px;
  }
  .card {
    position: absolute;
    width: 634px;
    height: 362px;
    left: 283px;
    overflow: hidden;
    background: var(--card-black);
  }
  .card--front { top: 172px; }
  .card--back { top: 642px; }

  .brand {
    position: absolute;
    display: flex;
    align-items: center;
    gap: 14px;
    font-family: "Montserrat", sans-serif;
    font-weight: 600;
    color: var(--brand-orange);
    letter-spacing: 1px;
    text-transform: uppercase;
  }
  .brand__mark {
    width: 22px;
    height: 22px;
    background: var(--brand-orange);
    flex: none;
  }
  .card--front .brand {
    left: 0;
    right: 0;
    top: 160px;
    justify-content: center;
    font-size: 31px;
  }

  .card__swoosh {
    position: absolute;
    inset: 0;
    width: 634px;
    height: 362px;
  }
  .card--back .brand {
    left: 42px;
    top: 140px;
    flex-direction: column;
    gap: 12px;
    font-size: 27px;
    line-height: 1.1;
    text-align: center;
  }
  .card--back .brand__mark { width: 26px; height: 26px; }

  .contact {
    position: absolute;
    right: 26px;
    top: 54px;
    text-align: right;
    font-family: "Open Sans", sans-serif;
    font-weight: 700;
    color: var(--text-light);
  }
  .contact__name {
    font-size: 24px;
    letter-spacing: 0.5px;
    text-transform: uppercase;
  }
  .contact__phone {
    margin-top: 4px;
    display: flex;
    align-items: center;
    justify-content: flex-end;
    gap: 12px;
    font-size: 25px;
    letter-spacing: 0.5px;
  }
  .contact__icon { width: 28px; height: 28px; }
</style>
</head>
<body>
<main class="canvas">

  <section class="card card--front" aria-label="Card front">
    <div class="brand">
      <span class="brand__mark"></span>
      <span class="brand__name">Corella Plumbing</span>
    </div>
  </section>

  <section class="card card--back" aria-label="Card back">
    <svg class="card__swoosh" viewBox="0 0 634 362" aria-hidden="true">
      <path d="M0 0 H276 C352 80 362 255 262 362 H0 Z" fill="var(--brand-blue)"/>
      <path d="M0 0 H264 C336 80 338 255 246 362 H0 Z" fill="var(--card-white)"/>
      <path d="M0 0 H188 C300 60 326 250 254 362 H0 Z" fill="var(--brand-orange)"/>
      <path d="M0 0 H172 C282 62 302 250 238 362 H0 Z" fill="var(--card-white)"/>
    </svg>

    <div class="brand">
      <span class="brand__mark"></span>
      <span class="brand__name">Corella<br>Plumbing</span>
    </div>

    <div class="contact">
      <p class="contact__name">Darrell Whitcombe</p>
      <p class="contact__phone">
        <svg class="contact__icon" viewBox="0 0 28 28" aria-hidden="true">
          <circle cx="14" cy="14" r="14" fill="var(--text-light)"/>
          <path d="M9.5 7.5 L12 7 L13.3 10.6 L11.6 12 C12.4 13.8 14 15.5 15.9 16.4 L17.3 14.7 L21 16 L20.5 18.5 C20.2 19.8 18.8 20.6 17.4 20.2 C12.6 18.9 9 15.3 7.8 10.6 C7.4 9.2 8.2 7.8 9.5 7.5 Z" fill="var(--card-black)"/>
        </svg>
        <span>0417305829</span>
      </p>
    </div>
  </section>

</main>
</body>
</html>
```